Retail Appliance Store Chain needs NEW business Card

Name of my company is Brandon's Appliances brandonsappliances.com is our website. . We are a 2 location brick and mortar, and online store selling premium, luxury, and normal household appliances, such as ovens, stoves, cooktops, dishwashers, refrigerators, washers and dryers, grills, air conditioners etc. The focus is on large kitchen appliances and laundry appliances.
Please visit http://brandonsappliances.com to get a feel for the business and branding.
I have attached the Brandon's Appliances logo (i do not have eps or psd or ai). And I have also attached our current business cards that we use. We have two versions. A double sided version for managers, and a one side version for regular employees.
Please submit BOTH one sided and two sided designs if possible.
Please keep consistent with the Brandon's Appliances logo, colors, etc.
I would prefer no rounded corners on the business card designs for printing costs.
Information on the cards (in no particular order):
Name - Employee Name
Business name - Brandon's Appliances
website - brandonsappliances.com
Email - Employee Email
2 Phone Numbers - store 1 address, store 2 address
2 Addresses - store 1 address, store 2 address

*do NOT need Fax #

Industry/Entity Type

Home Appliance

Contact Information for Business Card

Logo - Brandons Appliances Logo
Name - Employee Name
Email - Employee Email

Please no rounded corners. Standard US Business Card Size please.

Font styles to use
Serif
Sans Serif

Requirements
Must have
• colors and design that somewhat match the feel of current logo and website
Should not have
• No rounded corners.
No non-traditional business card size. US Standard Business Card Size only

```html
<!DOCTYPE html>
<html lang="en">
<head>
<meta charset="utf-8">
<title>Brandon's Appliances – Business Card</title>
<link rel="stylesheet" href="https://fonts.googleapis.com/css2?family=Open+Sans:wght@400;600;700;800&display=swap">
<style>
  :root {
    --brand-blue: #0b4a9a;
    --brand-blue-deep: #083f86;
    --brand-blue-soft: #1a5cb0;
    --paper: #ffffff;
    --backdrop: #e6e6e6;
    --ink-white: #ffffff;
  }
  * { box-sizing: border-box; margin: 0; padding: 0; }
  html, body {
    width: 1200px; height: 801px; overflow: hidden;
    background: var(--backdrop);
    font-family: "Open Sans", Arial, sans-serif;
  }
  .stage {
    width: 1200px; height: 801px;
    display: flex; align-items: center; justify-content: center; gap: 56px;
  }
  .card {
    position: relative;
    width: 525px; height: 300px;
    box-shadow: 0 6px 18px rgba(0,0,0,.18);
  }
  /* Front */
  .card--front { background: var(--paper); color: var(--brand-blue); }
  .front-logo {
    position: absolute; top: 40px; right: 34px;
    font-size: 27px; font-weight: 800; color: var(--brand-blue);
    display: flex; align-items: center; gap: 10px;
  }
  .front-logo .mark { width: 16px; height: 16px; background: var(--brand-blue); }
  .identity { position: absolute; left: 34px; top: 150px; }
  .identity .name { font-size: 21px; font-weight: 700; line-height: 1.1; }
  .identity .role, .identity .location { font-size: 14px; font-weight: 400; line-height: 1.3; }
  .divider {
    position: absolute; left: 34px; right: 34px; top: 222px;
    height: 1px; background: var(--brand-blue);
  }
  .contacts { position: absolute; left: 34px; top: 231px; list-style: none; }
  .contacts li {
    display: flex; align-items: center; gap: 9px;
    font-size: 14px; line-height: 20px;
  }
  .contacts svg { width: 11px; height: 11px; flex: none; }
  /* Back */
  .card--back { background: var(--brand-blue); color: var(--ink-white); }
  .back-logo {
    position: absolute; left: 0; right: 0; top: 92px; text-align: center;
    font-size: 40px; font-weight: 800; color: var(--brand-blue-soft);
  }
  .store { position: absolute; font-size: 14px; line-height: 19px; font-style: normal; }
  .store--one { left: 28px; bottom: 28px; }
  .store--two { right: 28px; top: 176px; text-align: right; }
</style>
</head>
<body>
<main class="stage">
  <section class="card card--front" aria-label="Business card front">
    <div class="front-logo"><span class="mark"></span>Brandon's Appliances</div>
    <div class="identity">
      <p class="name">Daniel Reyes</p>
      <p class="role">Bargain Basement Supervisor</p>
      <p class="location">Easton</p>
    </div>
    <div class="divider"></div>
    <ul class="contacts">
      <li>
        <svg viewBox="0 0 12 12" aria-hidden="true"><path d="M2.5 1l2 2.2-1.1 1.3a7 7 0 0 0 4.1 4.1l1.3-1.1 2.2 2-1.3 1.6C5 10.8 1.2 7 .9 2.3z" fill="currentColor"/></svg>
        (860) 555-0142 ext.10
      </li>
      <li>
        <svg viewBox="0 0 12 12" aria-hidden="true"><rect x=".7" y="2.2" width="10.6" height="7.6" fill="none" stroke="currentColor" stroke-width="1.2"/><path d="M.7 2.4L6 6.6l5.3-4.2" fill="none" stroke="currentColor" stroke-width="1.2"/></svg>
        danielr@brandonsappliances.com
      </li>
      <li>
        <svg viewBox="0 0 12 12" aria-hidden="true"><circle cx="6" cy="6" r="5.3" fill="currentColor"/><path d="M.7 6h10.6M6 .7c-2.4 2.8-2.4 7.8 0 10.6M6 .7c2.4 2.8 2.4 7.8 0 10.6" fill="none" stroke="#fff" stroke-width=".9"/></svg>
        www.brandonsappliances.com
      </li>
    </ul>
  </section>

  <section class="card card--back" aria-label="Business card back">
    <div class="back-logo">Brandon's Appliances</div>
    <address class="store store--two">
      27 Millbrook Ave.<br>Fairhaven, CT 06513<br>(860) 555-0178
    </address>
    <address class="store store--one">
      148 Harbor View St.<br>Easton, CT 06612<br>(860) 555-0142
    </address>
  </section>
</main>
</body>
</html>
```